Gaming Headset Packaging Design

We would like a gaming window box style packaging design for our gaming headset.

We want to use the packaging for 2-3 of our gaming headphone series and hence we would not like to put any product pictures on the packaging.

Size: (enclosed die-cut drawing) please feel free to modify the shape of the window
Material: E Flute Paper box
Type: Window Box style
Design features we prefer: gaming, playful, creative, trendy, High tech.
Requirement: AI file is preferred

Enclosed are a detailed description along with competitor designs and existing die-cut drawing (AI format) for your reference.

Any further questions, please feel free to ask.

```html
<!DOCTYPE html>
<html lang="en">
<head>
<meta charset="utf-8">
<title>Pro Gaming Headset 7.1 – Window Box Dieline</title>
<link rel="stylesheet" href="https://fonts.googleapis.com/css2?family=Montserrat:wght@500;600;700&display=swap">
<style>
  :root {
    --navy: #241e50;
    --navy-deep: #1d1747;
    --panel-blue: #273b8f;
    --wave-pink: #e9778a;
    --wave-violet: #5b2f6e;
    --white: #ffffff;
    --fold: rgba(255,255,255,0.18);
  }
  html, body {
    margin: 0;
    padding: 0;
    width: 1200px;
    height: 1200px;
    overflow: hidden;
    background: var(--white);
    font-family: "Montserrat", sans-serif;
  }
  .canvas {
    position: relative;
    width: 1200px;
    height: 1200px;
  }
  .dieline {
    position: absolute;
    inset: 0;
  }
  .brand {
    position: absolute;
    color: var(--white);
    text-align: center;
    line-height: 1;
  }
  .brand-name {
    font-weight: 700;
    font-size: 38px;
    letter-spacing: 0.5px;
  }
  .brand-line {
    font-weight: 600;
    font-size: 15px;
    margin-top: 4px;
  }
  .front-brand { left: 262px; top: 454px; width: 212px; }
  .lid-brand { left: 296px; top: 316px; width: 250px; transform: rotate(180deg); }
  .lid-brand .brand-name { font-size: 34px; }
  .lid-brand .brand-line { font-size: 13px; }

  .info-box {
    position: absolute;
    background: var(--panel-blue);
    color: var(--white);
    box-sizing: border-box;
  }
  .info-title {
    font-weight: 700;
    font-size: 17px;
    margin: 0 0 3px;
  }
  .features {
    left: 264px; top: 752px; width: 160px; height: 88px;
    padding: 4px 6px;
  }
  .features ul {
    margin: 0; padding: 0; list-style: none;
    font-size: 7.2px; font-weight: 500; line-height: 12.2px;
  }
  .features li::before { content: "• "; }
  .specs {
    left: 900px; top: 487px; width: 216px; height: 271px;
    padding: 4px 7px;
  }
  .specs p {
    margin: 0 0 14px;
    font-size: 6.8px; font-weight: 500; line-height: 12px;
    text-align: justify;
  }
  .specs strong { font-weight: 700; font-size: 8px; }
</style>
</head>
<body>
<div class="canvas">
  <svg class="dieline" width="1200" height="1200" viewBox="0 0 1200 1200">
    <defs>
      <linearGradient id="wave-fill" x1="0" y1="0" x2="0" y2="1">
        <stop offset="0" stop-color="#241e50" stop-opacity="0"/>
        <stop offset="0.45" stop-color="#5b2f6e" stop-opacity="0.8"/>
        <stop offset="0.7" stop-color="#c8657f" stop-opacity="0.75"/>
        <stop offset="1" stop-color="#241e50" stop-opacity="0.4"/>
      </linearGradient>
    </defs>

    <g class="flaps" fill="var(--navy)">
      <!-- lid tuck tab -->
      <path d="M258 248 V214 Q258 204 268 204 H587 Q597 204 597 214 V248 Z"/>
      <!-- lid -->
      <rect x="256" y="248" width="343" height="185"/>
      <!-- top dust flaps -->
      <polygon points="96,330 252,330 252,433 71,433 74,415"/>
      <polygon points="604,330 756,330 782,413 782,433 604,433"/>
      <!-- back lock tab -->
      <path d="M923 433 V404 Q923 398 929 398 H984 Q990 398 990 404 V433 Z"/>
      <!-- glue flap -->
      <polygon points="1128,433 1162,446 1162,831 1128,845"/>
      <!-- bottom flaps -->
      <polygon points="74,845 256,845 162,926 162,973 158,977 74,977"/>
      <polygon points="259,845 596,845 596,977 524,977 519,972 519,938 337,938 337,972 332,977 259,977"/>
      <polygon points="598,845 782,845 782,977 698,977 694,973 694,926"/>
      <polygon points="784,845 1128,845 1046,932 1046,971 1040,977 872,977 866,971 866,932"/>
    </g>

    <!-- main wrap band -->
    <rect class="body-band" x="71" y="433" width="1057" height="412" fill="var(--navy-deep)"/>
    <rect class="wave-art" role="img" aria-label="Pink and violet flowing particle wave artwork"
          x="71" y="540" width="1091" height="305" fill="url(#wave-fill)"/>

    <!-- product window -->
    <polygon class="window" fill="var(--white)"
      points="506,482 888,482 888,516 888,770 872,786 866,802 770,802 766,788 700,802 666,794 482,802 466,802 466,640 480,628 466,618 466,534"/>

    <g class="folds" stroke="var(--fold)" stroke-width="0.8" stroke-dasharray="3 3" fill="none">
      <line x1="256" y1="433" x2="256" y2="845"/>
      <line x1="599" y1="433" x2="599" y2="845"/>
      <line x1="782" y1="433" x2="782" y2="845"/>
      <line x1="1128" y1="433" x2="1128" y2="845"/>
      <line x1="71" y1="433" x2="1128" y2="433"/>
      <line x1="71" y1="845" x2="1128" y2="845"/>
      <line x1="256" y1="248" x2="599" y2="248"/>
      <line x1="923" y1="466" x2="990" y2="466"/>
    </g>
  </svg>

  <div class="brand lid-brand">
    <div class="brand-name">YOUR LOGO</div>
    <div class="brand-line">Pro Gaming Headset 7.1</div>
  </div>

  <div class="brand front-brand">
    <div class="brand-name">YOUR LOGO</div>
    <div class="brand-line">Pro Gaming Headset 7.1</div>
  </div>

  <div class="info-box features">
    <h3 class="info-title">Features:</h3>
    <ul>
      <li>Virtual 7.1 Surround Sound</li>
      <li>Dual Drivers on each ear for Accuracy</li>
      <li>3D Sound Vibration</li>
      <li>Bendable Stainless-Steel headband</li>
      <li>Soft and soothing earpads</li>
    </ul>
  </div>

  <div class="info-box specs">
    <h3 class="info-title">Specification:</h3>
    <p>Headphone Specification Speaker Diameter: Ø40mm Impedance: 32Ω ± 15 Sensitivity S.P.L: 113dB ± 3dB Rated Power: 20mW Aggregate capability: 30mW Frequency Response: 20-20kHz Plug Type: 3.5mm Stereo Microphone Specification Microphone Unit: Ø6 x 5mm Sensitivity S.P.L 34dB ± 3dB Impedance: &lt;2.2k Frequency Response: 30-16kHz Standard Operating Voltage: 4.5V S/N Ratio: Z 60dB Plug Type: 3.5mm Stereo</p>
    <p><strong>Warning:</strong> Adjust headphone's sound to a proper volume. Loud sound may damage your ears. For traffic safety never use the headset while driving.</p>
    <p><strong>Caution:</strong> If the user attempts to inspect or modify the product in any way we don't guarantee the performance of the product. Specifications and design are subject to possible modification notice due to improvements.</p>
  </div>
</div>
</body>
</html>
```